Branding product image: TOMBEL (Golden Papaya) in Plastic Cup (Ready to Eat)

The product is sliced Fruit in Light syrup
Flavour: TOMBEL (Golden Papaya)
The temporary product name: TOMBEL
I want the product design to be something 'fun', 'natural', and 'colourful'
The design concept could be anything depends on your imagination, but it must be eye catchy and attractive.
Basically, I want you to be creative in designing the logo and the overall graphic design for the label.
The measurement is 20 cm (Length) x 6,5 cm (Height)
The target customers are young and health conscious audiences (10 years - 65 years old).
Create something different. Something extraordinary.
Brief summary about the fruit:
This fruit only grows in certain part of the world. It grows in mountain area that is in tropical climate. The fruit flesh has a yellowish-golden color. It has an extraordinary taste (unlike normal papaya) and it suits very well with any dishes from cold appetizer, white/ red meat, desserts, and cocktails.
I need a packaging design for Fruit Cup productThe product is sliced Fruit in Light syrup.There will be various flavours i.e. apple, lychee, peach, papaya, etc.However, you may design the product using one sample flavour (i.e. papaya) first, as the designs of other flavours could be adjusted afterwards.The temporary product name is: RICCANAI want the product design to be something 'fun', 'natural', and 'colourful'.The design concept could be anything depends on your imagination. Basically, I want you to be creative in designing the logo and the overall graphic design for the label. - Create something different. Something extraordinary -Additional:The measurement is 20cm (Length) x 5cm (Height).The target customers are young audiences (10 years - 35 years old).The product design must stand out in the supermarket shelf.It must be eye catchy and attractive.Thank you,Harold-PLEASE REFER TO DESIGN SAMPLE ATTACHED TO HAVE A BETTER UNDERSTANDING FOR THE PRODUCT CONCEPT- Added Wednesday, September 17, 2014
Project Deadline Extended Reason: Haven't found a good design. Added Friday, September 19, 2014
Project Deadline Extended Reason: Need more time for designers to finalize and perfect the design.Thank you,Harold Added Monday, September 29, 2014
Project Deadline Extended Reason: I haven't found a great design yet. Added Tuesday, February 24, 2015
Reason: Getting better designs now. Still Open to new ideas while refining the latest designs from some designers.
Please do your best in submitting other great designs!

```html
<!DOCTYPE html>
<html lang="en">
<head>
<meta charset="utf-8">
<title>Lupedos Papaya – Fruit Cup Label</title>
<link href="https://fonts.googleapis.com/css2?family=Fredoka:wght@600&family=Crimson+Text:ital@1&display=swap" rel="stylesheet">
<style>
  :root {
    --page: #ffffff;
    --sky-top: #f4fffd;
    --aqua: #47e4da;
    --aqua-deep: #3fd9d0;
    --red: #ee4a27;
    --orange: #f7891f;
    --orange-left: #f27c1c;
    --sun: #f9b01b;
    --lime: #80f00a;
    --lime-deep: #3fdc1a;
    --soil: #5a2a12;
    --ink: #1a1a1a;
    --brand-red: #c8142e;
    --info-green: #3a9a2a;
    --slogan: #2a2a2a;
  }
  * { margin: 0; padding: 0; box-sizing: border-box; }
  html, body { width: 1200px; height: 391px; overflow: hidden; background: var(--page); }
  .label {
    position: absolute; left: 62px; top: 60px; width: 1096px; height: 276px;
    overflow: hidden;
    background: linear-gradient(to bottom, var(--sky-top) 0%, var(--aqua) 40%, var(--aqua) 100%);
  }
  .label > * { position: absolute; }
  .band-red { left: 0; top: 46px; width: 706px; height: 41px; background: var(--red); border-radius: 0 30px 30px 0; }
  .band-orange { left: 214px; top: 60px; width: 882px; height: 62px; background: var(--orange); border-radius: 32px 0 0 32px; }
  .band-orange-left { left: 0; top: 84px; width: 230px; height: 38px; background: var(--orange-left); }
  .sun { left: 476px; top: 6px; width: 132px; height: 132px; border-radius: 50%; background: var(--sun); box-shadow: 0 0 18px 6px rgba(255,255,255,.6); }
  .title-plate { left: 412px; top: 90px; width: 294px; height: 60px; background: var(--red); border-radius: 30px 30px 0 0; }
  .band-aqua { left: 0; top: 120px; width: 100%; height: 26px; background: var(--aqua); }
  .field { left: 0; top: 144px; width: 898px; height: 106px; background: var(--lime); }
  .field-bar { left: 226px; top: 223px; width: 516px; height: 19px; background: var(--lime-deep); border-radius: 10px; }
  .shore { left: 0; top: 246px; width: 100%; height: 30px; background: var(--aqua-deep); }
  .shore-curve { left: 230px; top: 238px; width: 866px; height: 40px; background: var(--aqua); border-radius: 40px 0 0 0; }
  .ground-left { left: 82px; top: 236px; width: 300px; height: 5px; background: var(--soil); border-radius: 3px; }
  .ground-right { left: 898px; top: 242px; width: 198px; height: 5px; background: var(--soil); }
  .palm-art { left: 4px; top: 6px; width: 234px; height: 234px; border-radius: 40% 40% 10% 10%;
    background: radial-gradient(ellipse at 45% 30%, #5ed61e 0%, #2fa81a 45%, rgba(47,168,26,0) 72%); }
  .bloom-art { left: 766px; top: 54px; width: 254px; height: 222px;
    background:
      radial-gradient(circle at 40% 78%, rgba(246,160,40,.95) 0%, rgba(246,160,40,.6) 28%, rgba(246,160,40,0) 42%),
      radial-gradient(circle at 72% 22%, rgba(250,238,40,.95) 0%, rgba(250,238,40,.5) 25%, rgba(250,238,40,0) 40%),
      radial-gradient(circle at 82% 62%, rgba(170,240,190,.9) 0%, rgba(120,230,150,.5) 25%, rgba(120,230,150,0) 42%); }
  .info-panel { left: 1020px; top: 18px; width: 74px; height: 252px; background: #fff;
    display: flex; align-items: center; justify-content: center; }
  .info-panel p { writing-mode: vertical-rl; transform: rotate(180deg);
    font: 11px/14px Arial, Helvetica, sans-serif; color: var(--info-green); }
  .flavour { left: 412px; top: 92px; width: 294px; text-align: center;
    font: 600 42px/1 "Fredoka", sans-serif; color: var(--ink);
    -webkit-text-stroke: 1px #fff; paint-order: stroke fill; text-shadow: 2px 2px 0 #fff; }
  .brand { left: 412px; top: 176px; width: 294px; text-align: center;
    font: 600 36px/1 "Fredoka", sans-serif; color: var(--brand-red); }
  .slogan { left: 250px; top: 250px; width: 640px; text-align: center;
    font: italic 18px/1 "Crimson Text", serif; color: var(--slogan); }
</style>
</head>
<body>
  <div class="label">
    <div class="band-red"></div>
    <div class="band-orange-left"></div>
    <div class="band-orange"></div>
    <div class="sun"></div>
    <div class="band-aqua"></div>
    <div class="title-plate"></div>
    <div class="field"></div>
    <div class="field-bar"></div>
    <div class="shore"></div>
    <div class="shore-curve"></div>
    <div class="ground-left"></div>
    <div class="ground-right"></div>
    <div class="palm-art" role="img" aria-label="Illustration of leaning coconut palm trees"></div>
    <div class="bloom-art" role="img" aria-label="Decorative bubbles and tropical blossoms in orange, yellow and green"></div>
    <div class="info-panel">
      <p>ingredients and product information<br>ingredients and product information<br>ingredients and product information</p>
    </div>
    <h1 class="flavour">Papaya</h1>
    <div class="brand">Lupedos</div>
    <p class="slogan">Slogan Lupedos fruit in light syrup.</p>
  </div>
</body>
</html>
```